Need Business Card for our Real Estate Business with Sales Executive's Picture

PANTONE 484 C ( RED)

PANTONE 2766 C ( BLUE

Industry/Entity Type

Real Estate

Contact Information for Business Card

Name, Mobile, email, & picture of Person
Agency Phone, address, Web address

Requirements
Must have
• Our Logo Colours, Agent Picture,

```html
<!DOCTYPE html>
<html lang="en">
<head>
<meta charset="utf-8">
<title>Dunmore Real Estate – Business Card</title>
<link href="https://fonts.googleapis.com/css2?family=Open+Sans:wght@400&display=swap" rel="stylesheet">
<style>
  :root {
    --page-bg: #c9ccd1;
    --navy: #061538;
    --band: #6b6d8c;
    --white: #ffffff;
    --ink-dark: #464646;
    --ink-mid: #6a6a6a;
    --rule: #9a9a9a;
    --photo-a: #2c4a8e;
    --photo-b: #c9a68c;
  }
  html, body {
    margin: 0;
    width: 1200px;
    height: 1000px;
    overflow: hidden;
    background: var(--page-bg);
    font-family: "Open Sans", sans-serif;
  }
  .card {
    position: absolute;
    left: 262px;
    width: 680px;
    height: 388px;
    background: var(--white);
    overflow: hidden;
  }
  .card--front { top: 85px; }
  .card--back  { top: 525px; background: var(--navy); }
  .card__art {
    position: absolute;
    inset: 0;
    width: 680px;
    height: 388px;
  }
  .agent-photo {
    position: absolute;
    left: 35px;
    top: 30px;
    width: 168px;
    height: 230px;
    background: linear-gradient(180deg, var(--photo-b) 0%, var(--photo-b) 30%, var(--photo-a) 55%, var(--photo-a) 100%);
  }
  .agent-name {
    position: absolute;
    left: 211px;
    top: 38px;
    margin: 0;
    font-size: 24px;
    font-weight: 400;
    color: var(--ink-dark);
    line-height: 1.2;
  }
  .agent-title {
    position: absolute;
    left: 211px;
    top: 73px;
    margin: 0;
    font-size: 19px;
    color: var(--ink-dark);
  }
  .divider {
    position: absolute;
    left: 211px;
    top: 112px;
    width: 432px;
    height: 2px;
    background: var(--rule);
  }
  .agency-address {
    position: absolute;
    left: 211px;
    top: 128px;
    margin: 0;
    font-size: 19px;
    color: var(--ink-mid);
  }
  .contact-list {
    position: absolute;
    left: 286px;
    top: 256px;
    margin: 0;
    padding: 0;
    list-style: none;
  }
  .contact-list li {
    display: flex;
    align-items: center;
    height: 37px;
    font-size: 19px;
    color: var(--white);
  }
  .contact-list svg {
    width: 18px;
    height: 18px;
    margin-right: 22px;
  }
  .brand-name {
    position: absolute;
    margin: 0;
    color: var(--white);
    font-weight: 400;
    letter-spacing: 2px;
    text-align: center;
  }
  .brand-name--front {
    left: 33px;
    top: 318px;
    width: 200px;
    font-size: 20px;
  }
  .brand-name--back {
    left: 0;
    top: 160px;
    width: 680px;
    font-size: 44px;
    letter-spacing: 4px;
  }
</style>
</head>
<body>

<section class="card card--front">
  <div class="agent-photo" role="img" aria-label="Portrait photo of the sales executive in a navy suit"></div>
  <svg class="card__art" viewBox="0 0 680 388" aria-hidden="true">
    <path d="M0,236 C90,268 200,262 320,228 C430,196 560,158 680,202 L680,388 L0,388 Z" fill="#ffffff"/>
    <path d="M0,242 C90,274 200,268 320,234 C430,202 560,164 680,208 L680,388 L0,388 Z" fill="var(--navy)"/>
  </svg>

  <h1 class="agent-name">Name of Sales Executive's</h1>
  <p class="agent-title">Sales Executive</p>
  <div class="divider"></div>
  <p class="agency-address">address of Dunmore Real Estate</p>

  <ul class="contact-list">
    <li>
      <svg viewBox="0 0 18 18"><circle cx="9" cy="9" r="7.5" fill="none" stroke="#fff" stroke-width="1.5"/><path d="M6,5.5 L7.5,5 L8.3,7 L7.4,7.8 C7.9,9 8.9,10 10.2,10.6 L11,9.7 L13,10.5 L12.5,12 C9,12.3 5.7,9 6,5.5 Z" fill="#fff"/></svg>
      mobile / agency phone
    </li>
    <li>
      <svg viewBox="0 0 18 18"><rect x="2" y="4.5" width="14" height="9" fill="#fff"/><path d="M2,4.5 L9,10 L16,4.5" fill="none" stroke="var(--navy)" stroke-width="1.2"/></svg>
      dunmore@email.com
    </li>
    <li>
      <svg viewBox="0 0 18 18"><circle cx="9" cy="9" r="7.5" fill="#fff"/><path d="M1.5,9 H16.5 M9,1.5 V16.5 M3,5.5 H15 M3,12.5 H15" stroke="var(--navy)" stroke-width="1"/><ellipse cx="9" cy="9" rx="3.2" ry="7.5" fill="none" stroke="var(--navy)" stroke-width="1"/></svg>
      www.web address.com
    </li>
  </ul>

  <p class="brand-name brand-name--front">DUNMORE</p>
</section>

<section class="card card--back">
  <svg class="card__art" viewBox="0 0 680 388" aria-hidden="true">
    <path d="M0,250 C140,212 300,232 450,275 C560,305 630,300 680,285 L680,388 L0,388 Z" fill="var(--band)"/>
    <path d="M0,282 C150,242 320,262 460,302 C570,332 640,322 680,310 L680,388 L0,388 Z" fill="#ffffff"/>
  </svg>
  <p class="brand-name brand-name--back">DUNMORE</p>
</section>

</body>
</html>
```